Brisk Motion Flyer - Physiotherapy company

I am looking for a two-sided flyer (4"x8") that can be easily posted on cork boards or displayed as needed to provide information about my business. I would like to use the colors found in my logo (see attached) along with white and black. Please have a look at my website for ideas of how I would like the color schemes etc (www.briskmotion.example). I would like it to follow the same style as my website.<br/><br/>FRONT SIDE<br/>I am hoping to have the name of our business "Brisk Motion" with our slogan "Boreal Physiotherapy - Rehab and Recovery Above the Line (degrees symbol)" underneath. Somewhere above or around this I would like my logo (see attached). <br/><br/>Below that I would like a title "Services Provided" and then listed: <br/>Mobile Services<br/>Clinic<br/>Telehealth<br/><br/>Below that, I would like another title "Treatments Offered" and then listed: <br/>Hands-on manual therapy<br/>Intramuscular Stimulation (IMS)<br/>Acupuncture<br/>Athletic taping<br/>Injury/condition education<br/>Supervised exercise<br/><br/>Below that I would like "Contact Us":<br/>Brisk Motion<br/>www.BriskMotion.example<br/>Book online through https://briskmotion.bookerly.example/<br/>physio@briskmotion.example<br/>867-555-0148<br/>Direct Billing offered for most extended health providers<br/>(friendwall, Pictagram logo, movetrak logo (see attached) on bottom maybe in corner or centered)<br/><br/>BACK SIDE<br/><br/>I would like the logo on there once again maybe. Then I would like these three information sections one on top of the other spaced out appropriately.<br/><br/>Image (needling image) (see attached)<br/>Title: Mobile Physiotherapy<br/>The information below title: If you want to keep moving and need some help, but your current condition makes it difficult or unsafe to travel to and from a clinic to see a physiotherapist, that’s where we come in. We make it easy by offering a mobile service that provides exceptional one-on-one physiotherapy assessment and treatment in the comfort of your own home. There is a small fee to access mobile services. <br/><br/>Image (Hands on knee image) (see attached)<br/>Title: Clinic<br/>The information below title: If you have an injury that is causing you pain or restricting you from doing the activities that you want to do then physiotherapy can help. A traditional approach to physiotherapy where you come to our clinic and we provide one to one education and hands on therapy. <br/><br/>Image (computer, tablet etc) (see attached)<br/>Title: Telehealth<br/>The information below title: If you live outside of Whitehorse or just want easy access to a physiotherapist from the comfort of your home, then Telehealth is for you. Telehealth involves meeting with your physiotherapist using real-time technology, similar to ViewTalk. Brisk Motion utilizes Movetrakker for exercise prescription, pain tracking and telehealth. Through Movetrakker or it’s Kinetapp you can discuss your treatment plan, diagnoses, exercises, daily activities or any other questions you may have directly with a physiotherapist.<br/><br/><br/><br/>

Industry/Entity Type

Healthcare

Colors

Designer to choose colors to be used in the design.

Requirements
Must have
• Follow the same colors and schemes of my website (www.briskmotion.example)
• Keep it clean and concise
Nice to have
• Images might not fit because I don't want it too cluttered.
Should not have
• Too busy

```html
<!DOCTYPE html>
<html lang="en">
<head>
<meta charset="utf-8">
<title>Brisk Motion – Flyer Front</title>
<link href="https://fonts.googleapis.com/css2?family=Archivo+Black&family=Cabin:wght@400;500;600;700&display=swap" rel="stylesheet">
<style>
  :root {
    --paper: #f3f3f3;
    --green-deep: #0c4d40;
    --blue: #2a4a7d;
    --app-green: #2b9a78;
    --white: #ffffff;
  }
  * { margin: 0; padding: 0; box-sizing: border-box; }
  html, body { width: 1200px; height: 2400px; overflow: hidden; background: var(--paper); }
  .flyer {
    position: relative;
    width: 1200px;
    height: 2400px;
    background: var(--paper);
    font-family: "Cabin", Arial, sans-serif;
    color: var(--green-deep);
    overflow: hidden;
  }
  .flyer__shapes { position: absolute; inset: 0; width: 1200px; height: 2400px; }
  .line {
    position: absolute;
    left: 0; right: 0;
    text-align: center;
    transform: translateY(-50%);
    white-space: nowrap;
  }
  .brand-mark {
    position: absolute;
    left: 530px; top: 110px;
    width: 140px; height: 140px;
    background: var(--blue);
  }
  .brand-name {
    font-family: "Archivo Black", Arial, sans-serif;
    color: var(--green-deep);
    line-height: 1;
  }
  .brand-name--main { font-size: 112px; letter-spacing: 14px; padding-left: 14px; }
  .brand-name--sub { font-size: 54px; letter-spacing: 26px; padding-left: 26px; }
  .tagline {
    font-family: "Archivo Black", Arial, sans-serif;
    color: var(--green-deep);
    font-size: 52px;
    line-height: 1;
  }
  .section-title {
    color: var(--white);
    font-weight: 600;
    font-size: 57px;
    letter-spacing: -0.5px;
  }
  .list-item {
    color: var(--white);
    font-size: 48px;
    letter-spacing: 2px;
    word-spacing: 6px;
  }
  .pill {
    position: absolute;
    background: var(--green-deep);
    color: var(--white);
    border-radius: 40px;
    display: flex;
    align-items: center;
    justify-content: center;
    font-weight: 500;
    letter-spacing: -0.5px;
  }
  .pill--contact { left: 419px; top: 1824px; width: 336px; height: 77px; font-size: 41px; }
  .pill--booking { left: 288px; top: 1978px; width: 603px; height: 66px; font-size: 39px; }
  .contact-detail { font-weight: 700; font-size: 37px; color: var(--green-deep); }
  .billing-note { font-weight: 500; font-size: 33px; color: var(--blue); }
  .social {
    position: absolute;
    top: 2333px;
    transform: translateY(-50%);
    display: flex;
    align-items: center;
    gap: 12px;
    font-size: 38px;
    font-weight: 500;
    color: var(--blue);
  }
  .social__dot { width: 88px; height: 88px; border-radius: 50%; background: var(--blue); }
  .social__square { width: 68px; height: 68px; border-radius: 14px; background: var(--blue); }
  .social--friendwall { left: 40px; }
  .social--pictagram { left: 480px; }
  .social--kinetapp { left: 877px; font-size: 60px; font-weight: 700; color: var(--app-green); }
</style>
</head>
<body>
<main class="flyer">
  <svg class="flyer__shapes" viewBox="0 0 750 1500" preserveAspectRatio="none">
    <defs>
      <linearGradient id="bandPhoto" x1="0" y1="0" x2="1" y2="1">
        <stop offset="0" stop-color="#2d6c5c"/>
        <stop offset="0.5" stop-color="#225f50"/>
        <stop offset="1" stop-color="#1a5546"/>
      </linearGradient>
    </defs>
    <polygon class="band" points="0,455 750,520 750,1142 0,1084" fill="url(#bandPhoto)"
      role="img" aria-label="Photo of a physiotherapist's hands treating a patient's knee, tinted green"/>
    <polygon class="accent accent--top" points="460,487 750,466 750,511" fill="#2a4a7d"/>
    <polygon class="accent accent--bottom" points="0,1097 255,1117 0,1138" fill="#2a4a7d"/>
  </svg>

  <div class="brand-mark" aria-hidden="true"></div>
  <div class="line brand-name brand-name--main" style="top:368px;">BRISK</div>
  <div class="line brand-name brand-name--sub" style="top:464px;">MOTION</div>

  <div class="line tagline" style="top:557px;">Boreal Physiotherapy</div>
  <div class="line tagline" style="top:637px;">Rehab and Recovery Above the Line</div>

  <div class="line section-title" style="top:910px;">SERVICES PROVIDED</div>
  <div class="line list-item" style="top:997px;">Mobile Services</div>
  <div class="line list-item" style="top:1072px;">Clinic</div>
  <div class="line list-item" style="top:1147px;">Telehealth</div>

  <div class="line section-title" style="top:1296px;">TREATMENTS OFFERED</div>
  <div class="line list-item" style="top:1378px;">Hands-on manual therapy</div>
  <div class="line list-item" style="top:1453px;">Intramuscular Stimulation (IMS)</div>
  <div class="line list-item" style="top:1528px;">Athletic taping</div>
  <div class="line list-item" style="top:1603px;">Injury/condition education</div>
  <div class="line list-item" style="top:1678px;">Supervised exercise</div>

  <div class="pill pill--contact">CONTACT US</div>
  <div class="line contact-detail" style="top:1934px;">www.BriskMotion.example</div>
  <div class="pill pill--booking">BOOK ONLINE THROUGH</div>
  <div class="line contact-detail" style="top:2077px;">https://briskmotion.bookerly.example</div>
  <div class="line contact-detail" style="top:2125px;">physio@briskmotion.example</div>
  <div class="line contact-detail" style="top:2174px;">867-555-0148</div>
  <div class="line billing-note" style="top:2226px;">Direct Billing offered for most extended health providers</div>

  <div class="social social--friendwall"><span class="social__dot"></span>Brisk Motion</div>
  <div class="social social--pictagram"><span class="social__square"></span>BriskMotion</div>
  <div class="social social--kinetapp">Kinetapp</div>
</main>
</body>
</html>
```